Hearth Keepers Brochure - marketing an innovative home maintenance subscription program

We would like a brochure for this new service offering.
Hearth Keepers offers a subscription based home maintenance program that is quite unique. Everyone goes to the dentist for regular checkups and cleanings, or takes their car for oil changes, but too few pay that much attention to their largest asset - their home. So we fill that niche. We need a good brochure to promote the quarterly maintenance and our general contracting services.

Target Market(s)

Upper-Middle Class, SF Bay Area, Home Owner. Techies without know-how or time, single women, and elderly families or those with vacation homes.

Industry/Entity Type

Handyman and general contracting (residential construction and maintenance)

Font styles to use
Serif

Colors
0054AA
0677BA
7BADD7
CADEEF
E8F1F8

Requirements
Must have
• Basic contact info for www.HearthKeepersco.example, some sort of hook, logo, etc.
Nice to have
• Something awesome!
Should not have
• Want classy, not cheap or flashy. Must have good balance for high-end homeowners in San Francisco Bay Area.

```html
<!DOCTYPE html>
<html lang="en">
<head>
<meta charset="utf-8">
<title>Hearth Keepers Brochure</title>
<link href="https://fonts.googleapis.com/css2?family=Playfair+Display:wght@700&family=Source+Serif+4:wght@400;600&display=swap" rel="stylesheet">
<style>
  :root {
    --deep: #0054aa;
    --mid: #0677ba;
    --sky: #7badd7;
    --mist: #cadeef;
    --frost: #e8f1f8;
    --paper: #ffffff;
    --ink: #1c2a3a;
    --label: #1f3550;
  }
  * { margin: 0; padding: 0; box-sizing: border-box; }
  html, body { width: 1200px; height: 800px; overflow: hidden; background: var(--frost); }
  .brochure {
    position: absolute; left: 100px; top: 10px;
    width: 1000px; height: 780px; background: var(--paper); overflow: hidden;
    box-shadow: 0 2px 10px rgba(0,0,0,.12);
  }
  .backdrop { position: absolute; inset: 0; }
  .cover-title {
    position: absolute; left: 24px; top: 28px;
    font-family: "Playfair Display", Georgia, serif; font-weight: 700;
    font-size: 33px; line-height: 40px; color: var(--mist);
    text-transform: uppercase; letter-spacing: .3px;
  }
  .intro {
    position: absolute; left: 14px; top: 268px; width: 420px;
    font-family: "Source Serif 4", Georgia, serif; font-size: 18px; line-height: 25px; color: var(--ink);
  }
  .service { position: absolute; display: flex; align-items: center; }
  .service .thumb {
    width: 158px; height: 102px; border: 3px solid var(--mid);
    background: linear-gradient(135deg, #8a8f96, #c9c6c0);
  }
  .service .name {
    margin-left: 14px; font-family: "Source Serif 4", Georgia, serif; font-weight: 600;
    font-size: 15px; line-height: 21px; color: var(--label); text-transform: uppercase;
  }
  .brand { position: absolute; left: 20px; top: 716px; }
  .brand .row { display: flex; align-items: center; gap: 8px; }
  .brand .mark { width: 24px; height: 24px; background: var(--deep); }
  .brand .name {
    font-family: "Playfair Display", Georgia, serif; font-weight: 700;
    font-size: 26px; line-height: 30px; color: var(--deep); text-transform: uppercase;
  }
  .brand .web {
    display: block; margin-top: 4px; margin-left: 32px;
    font-family: "Source Serif 4", Georgia, serif; font-size: 14px; line-height: 18px; color: var(--mid);
  }
  .promise {
    position: absolute; left: 722px; top: 262px; width: 270px;
    font-family: "Source Serif 4", Georgia, serif; color: #fff; font-size: 13.5px; line-height: 18.5px;
  }
  .promise h2 {
    font-family: "Playfair Display", Georgia, serif; font-weight: 700; font-size: 32px; line-height: 38px;
    color: var(--mist); margin-bottom: 10px; text-transform: uppercase;
  }
  .promise p { margin-bottom: 14px; }
  .promise p.lead { margin-bottom: 8px; }
  .cta { position: absolute; left: 722px; top: 714px; display: flex; align-items: center; gap: 12px; }
  .cta .mark { width: 28px; height: 28px; background: var(--sky); }
  .cta .line {
    font-family: "Playfair Display", Georgia, serif; font-weight: 700;
    font-size: 17px; line-height: 23px; color: var(--mist); text-transform: uppercase;
  }
</style>
</head>
<body>
<div class="brochure">
  <svg class="backdrop" width="1000" height="780" viewBox="0 0 1000 780">
    <defs>
      <linearGradient id="plumbingTone" x1="0" y1="0" x2="1" y2="1">
        <stop offset="0" stop-color="#3b3a38"/>
        <stop offset=".45" stop-color="#b9b7b2"/>
        <stop offset="1" stop-color="#6b5a4a"/>
      </linearGradient>
    </defs>
    <rect x="0" y="0" width="1000" height="260" fill="url(#plumbingTone)" role="img" aria-label="Photo of a gloved hand tightening a pipe fitting under a sink"/>
    <path d="M0,190 L230,165 C330,240 520,262 700,232 C840,208 940,120 1000,45 L1000,780 L0,780 Z" fill="var(--paper)"/>
    <path d="M470,252 C560,256 640,250 700,240 C840,214 940,130 1000,62 L1000,780 L695,780 L695,248 Z" fill="var(--deep)"/>
    <path d="M230,165 C330,240 520,262 700,232 C840,208 940,120 1000,45" fill="none" stroke="var(--sky)" stroke-width="9"/>
    <rect x="695" y="245" width="305" height="535" fill="var(--deep)"/>
    <circle cx="90" cy="10" r="210" fill="var(--deep)"/>
    <circle cx="90" cy="10" r="198" fill="none" stroke="var(--mid)" stroke-width="2"/>
    <path d="M255,780 C380,750 540,742 695,758 L695,780 Z" fill="var(--deep)"/>
    <path d="M255,774 C380,744 540,736 695,752" fill="none" stroke="var(--sky)" stroke-width="6"/>
  </svg>

  <h1 class="cover-title">Home<br>Maintenance<br>&amp; Service</h1>

  <p class="intro">Hearth Keepers can also help with larger home improvements such as:</p>

  <div class="service" style="left:13px;top:345px"><div class="thumb" role="img" aria-label="Photo of a bright remodeled kitchen"></div><div class="name">Kitchen and<br>Bath Remodels</div></div>
  <div class="service" style="left:13px;top:465px"><div class="thumb" role="img" aria-label="Photo of a worker using a nail gun on decking"></div><div class="name">New Landscape<br>Installations<br>and Decks</div></div>
  <div class="service" style="left:13px;top:585px"><div class="thumb" role="img" aria-label="Photo of a door lock being installed with a drill"></div><div class="name">New Roofs,<br>Siding, Doors<br>and Windows</div></div>
  <div class="service" style="left:353px;top:345px"><div class="thumb" role="img" aria-label="Photo of a drainage pipe laid in a trench"></div><div class="name">Site<br>Drainage</div></div>
  <div class="service" style="left:353px;top:468px"><div class="thumb" role="img" aria-label="Photo of a gloved hand fitting an air vent cover"></div><div class="name">Indoor Air<br>Quality<br>Improvements</div></div>
  <div class="service" style="left:353px;top:590px"><div class="thumb" role="img" aria-label="Photo of an attic with exposed roof rafters"></div><div class="name">Home Comfort<br>and HVAC<br>Upgrades</div></div>

  <div class="brand">
    <div class="row"><span class="mark"></span><span class="name">Hearth Keepers</span></div>
    <span class="web">www.HearthKeepersco.example</span>
  </div>

  <section class="promise">
    <h2>We Maintain<br>Your Home</h2>
    <p class="lead">so you don’t have to.</p>
    <p>You take your car in for oil changes.</p>
    <p>You go to the dentist for check-ups. But when was the last time you had your home inspected, or managed, to check over 250 items off your to-do list?</p>
    <p>Hearth Keeping is a philosophy and lifestyle change. We keep your largest asset in great condition, and let you take back your weekends.</p>
    <p>Our unique subscription service combines quarterly inspections and handyman repairs.</p>
    <p>Don’t climb that rickety ladder to clean your gutters or start projects you can’t finish.</p>
  </section>

  <div class="cta"><span class="mark"></span><span class="line">Our team is ready to<br>care for your home.</span></div>
</div>
</body>
</html>
```